Bref créative
plumbing
KORLITH PLUMBING INC
Use same font as used in my logo
MARTIN OKAFOR
SERVICE MANAGER
3815 QUILLEN RIDGE DR LAS VEGAS NEVADA 89104
MOKAFOR@KORLITHPLUMBINGINC.EXAMPLE
WWW.KORLITHPLUMBINGINC.EXAMPLE
NV CL #41826
PLEASE USE COMPANY LOGO

```html
<!DOCTYPE html>
<html lang="en">
<head>
<meta charset="utf-8">
<title>Korlith Plumbing Inc – Business Card</title>
<link href="https://fonts.googleapis.com/css2?family=Montserrat:wght@600;800&family=Open+Sans:ital,wght@0,400;0,600;1,400&display=swap" rel="stylesheet">
<style>
  :root{
    --bg:#e6e7e9;
    --paper:#ffffff;
    --blue:#1f8fd8;
    --blue-deep:#0d6fb8;
    --blue-light:#3ba9ec;
    --navy:#1b2a3a;
    --ink:#2f3b47;
    --muted:#5a6672;
    --dark:#1c1f23;
  }
  *{margin:0;padding:0;box-sizing:border-box}
  html,body{width:1200px;height:895px;overflow:hidden;background:var(--bg)}
  .canvas{position:relative;width:1200px;height:895px}
  .card{position:absolute;top:290px;width:530px;height:303px;border-radius:4px;overflow:hidden;box-shadow:0 2px 6px rgba(0,0,0,.15)}
  .card--front{left:45px;background:var(--paper)}
  .card--back{left:625px;background:radial-gradient(ellipse at 40% 35%,var(--blue-light) 0%,var(--blue) 55%,var(--blue-deep) 100%)}

  .front-bands{position:absolute;left:0;bottom:0;width:530px;height:60px}

  .brand{position:absolute;left:138px;top:44px;display:flex;align-items:center;gap:12px}
  .brand__dot{width:34px;height:34px;border-radius:50%;background:var(--blue)}
  .brand__name{font-family:"Montserrat",sans-serif;font-weight:800;font-size:25px;letter-spacing:1px;line-height:1.05;color:var(--navy)}

  .person{position:absolute;left:40px;top:130px;font-family:"Open Sans",sans-serif;color:var(--ink)}
  .person__name{font-size:15px;font-weight:600;color:var(--blue)}
  .person__title{font-size:10px;font-style:italic;color:var(--muted);margin-bottom:12px}
  .person__address{font-size:11.5px;line-height:1.45}

  .contacts{position:absolute;left:262px;top:128px;list-style:none;font-family:"Open Sans",sans-serif;font-size:10.5px;color:var(--ink)}
  .contacts li{display:flex;align-items:center;gap:8px;height:20px}
  .contacts svg{width:13px;height:13px;flex:none}

  .back-name{position:absolute;left:0;right:0;top:92px;text-align:center;font-family:"Montserrat",sans-serif;font-weight:800;font-size:34px;letter-spacing:2px;color:rgba(255,255,255,.16)}
  .back-url{position:absolute;right:34px;bottom:60px;font-family:"Open Sans",sans-serif;font-size:11px;letter-spacing:2px;color:#eaf5fd}
</style>
</head>
<body>
<main class="canvas">

  <section class="card card--front" aria-label="Card front">
    <svg class="front-bands" viewBox="0 0 530 60" preserveAspectRatio="none" aria-hidden="true">
      <defs>
        <linearGradient id="bandBlue" x1="0" y1="0" x2="1" y2="0">
          <stop offset="0" stop-color="#3ba9ec"/>
          <stop offset="1" stop-color="#0d6fb8"/>
        </linearGradient>
        <linearGradient id="bandDark" x1="0" y1="0" x2="1" y2="0">
          <stop offset="0" stop-color="#6b7178"/>
          <stop offset=".5" stop-color="#1c1f23"/>
          <stop offset="1" stop-color="#3a3f45"/>
        </linearGradient>
      </defs>
      <path d="M0 36 L300 36 L330 60 L0 60 Z" fill="url(#bandBlue)"/>
      <path d="M300 36 L530 28 L530 60 L330 60 Z" fill="url(#bandDark)"/>
    </svg>

    <div class="brand">
      <span class="brand__dot" aria-hidden="true"></span>
      <span class="brand__name">KORLITH<br>PLUMBING INC</span>
    </div>

    <div class="person">
      <p class="person__name">Martin Okafor</p>
      <p class="person__title">Service Manager</p>
      <p class="person__address">3815 Quillen Ridge Dr<br>Las Vegas Nevada 89104</p>
    </div>

    <ul class="contacts">
      <li>
        <svg viewBox="0 0 16 16"><circle cx="8" cy="8" r="8" fill="#1f8fd8"/><path d="M5.3 4.2l1.4 1.6-.7 1.1c.6 1.2 1.5 2.1 2.7 2.7l1.1-.7 1.6 1.4-.8 1.3C7.6 11.4 4.6 8.4 4 5l1.3-.8z" fill="#fff"/></svg>
        702-555-0147
      </li>
      <li>
        <svg viewBox="0 0 16 16"><circle cx="8" cy="8" r="8" fill="#1f8fd8"/><rect x="5.5" y="3.5" width="5" height="9" rx="1" fill="#fff"/><rect x="6.4" y="4.6" width="3.2" height="5.6" fill="#1f8fd8"/></svg>
        702-555-0182
      </li>
      <li>
        <svg viewBox="0 0 16 16"><circle cx="8" cy="8" r="8" fill="#1f8fd8"/><rect x="4" y="5" width="8" height="6" fill="#fff"/><path d="M4 5l4 3.2L12 5" stroke="#1f8fd8" stroke-width="1" fill="none"/></svg>
        mokafor@korlithplumbinginc.example
      </li>
      <li>
        <svg viewBox="0 0 16 16"><circle cx="8" cy="8" r="8" fill="#1f8fd8"/><circle cx="8" cy="8" r="4" fill="none" stroke="#fff" stroke-width="1.1"/><path d="M4 8h8M8 4c-2 2.4-2 5.6 0 8M8 4c2 2.4 2 5.6 0 8" stroke="#fff" stroke-width=".9" fill="none"/></svg>
        www.korlithplumbinginc.example
      </li>
    </ul>
  </section>

  <section class="card card--back" aria-label="Card back">
    <p class="back-name">KORLITH PLUMBING INC</p>
    <p class="back-url">www.KorlithPlumbingInc.example</p>
  </section>

</main>
</body>
</html>
```